Roofing Company Now Hiring and Call Now Facebook Ads

Trying to hire new sales reps in our Alabama market to add to our growing team. This is a great opportunity for any one looking for a career change or looking to add time back to the time they get to spend at home with their families. This is a chance to build a career in one of the fastest growing industries in the country and build financial freedom and a solid future for your family while easily making 6 figures yearly. Sales reps get to set their own schedule, take vacations when they want, and could even choose if they wanted to work in the summer or the winter seasons if they dont like the heat/cold environment. Sales reps are commission based with bonus/incentives for completing task and assignments weekly.

"Let's Talk About Your Roof!" Schedule a free Roof Inspection today!

Needing facebook ads for hiring and a few ads templates for daily post regarding roof inspections and roof replacements, if they are editable it would be easier for me to manage a few templates. This project needs to have a swag/cleanish look that attracts the younger group of people but still make the older group of customer think, man these guys have some solid looking things going on and looks like a well managed and built company. We also target the upper scale areas when seeking customers.

Lets see what yall got! lets Gooo!

Target Market(s)

Property owners, sales reps, homeowners, property managers, job seekers

Industry/Entity Type

Roofing Contractor Storm Restoration Contractor, Construction Contractor

Font styles to use
Sans Serif

Colors
EB3D1F
EC4F4E
F09395
F8D3D4
FCEDEE

Requirements
Must have
• Clean modern professional look with visible red and black colors, we like white too.
Nice to have
• red, black, white, popping eye catching colors.
Should not have
• wrong color red, red is more of a kelvard herons red, please stay away from the pinkish red.

```html
<!DOCTYPE html>
<html lang="en">
<head>
<meta charset="utf-8">
<title>Stonecrest Roofing – We're Hiring</title>
<link href="https://fonts.googleapis.com/css2?family=Montserrat:wght@500;600;700;800&display=swap" rel="stylesheet">
<style>
  :root {
    --brand-red: #e31c45;
    --brand-red-deep: #c8103a;
    --brand-red-dark: #8e1b36;
    --scene-grey: #6b6b68;
    --white: #ffffff;
  }
  html, body {
    margin: 0;
    padding: 0;
    width: 1200px;
    height: 439px;
    overflow: hidden;
    background: var(--white);
  }
  .banner {
    position: relative;
    width: 1200px;
    height: 439px;
    overflow: hidden;
    background: var(--brand-red);
    font-family: "Montserrat", sans-serif;
    color: var(--white);
  }
  .banner-art {
    position: absolute;
    inset: 0;
  }
  .brand {
    position: absolute;
    left: 72px;
    top: 60px;
    width: 136px;
    text-align: center;
    font-weight: 700;
    line-height: 1;
  }
  .brand-name {
    display: block;
    font-size: 15px;
    letter-spacing: 0.6px;
  }
  .brand-sub {
    display: block;
    margin-top: 6px;
    font-size: 8px;
    letter-spacing: 3.5px;
  }
  .eyebrow {
    position: absolute;
    left: 62px;
    top: 124px;
    margin: 0;
    font-size: 29px;
    font-weight: 500;
    letter-spacing: 2.2px;
  }
  .headline {
    position: absolute;
    left: 58px;
    top: 160px;
    margin: 0;
    font-size: 84px;
    font-weight: 800;
    line-height: 1;
  }
  .market {
    position: absolute;
    left: 65px;
    top: 247px;
    margin: 0;
    font-size: 30px;
    font-weight: 500;
    letter-spacing: 2.4px;
  }
  .pitch {
    position: absolute;
    left: 64px;
    top: 302px;
    margin: 0;
    font-size: 11.5px;
    font-weight: 700;
    letter-spacing: 1.1px;
    line-height: 17px;
  }
  .call-line {
    position: absolute;
    left: 64px;
    top: 364px;
    margin: 0;
    font-size: 37px;
    font-weight: 700;
    letter-spacing: 1.5px;
    color: var(--brand-red);
  }
</style>
</head>
<body>
<main class="banner">
  <svg class="banner-art" width="1200" height="439" viewBox="0 0 1200 439">
    <defs>
      <linearGradient id="sceneFade" x1="0" y1="0" x2="1" y2="0">
        <stop offset="0" stop-color="#e31c45" stop-opacity="0"/>
        <stop offset="0.45" stop-color="#8a4a58"/>
        <stop offset="0.8" stop-color="#6b6b68"/>
        <stop offset="1" stop-color="#5f605c"/>
      </linearGradient>
      <linearGradient id="workerTones" x1="0" y1="0" x2="0" y2="1">
        <stop offset="0" stop-color="#8c8a86"/>
        <stop offset="0.35" stop-color="#b98a6c"/>
        <stop offset="1" stop-color="#d8773a"/>
      </linearGradient>
    </defs>

    <rect class="city-scene" x="480" y="0" width="720" height="439" fill="url(#sceneFade)" role="img" aria-label="Photo of a city rooftop with office buildings"/>

    <polygon class="headline-band" points="0,164 600,164 740,250 720,270 0,242" fill="var(--brand-red-deep)" opacity="0.8"/>

    <polygon class="accent-band" points="464,439 1200,5 1200,206 798,439" fill="var(--brand-red)"/>
    <polygon class="accent-shadow" points="840,439 1000,345 1040,439" fill="var(--brand-red-dark)" opacity="0.6"/>

    <rect class="worker-photo" x="820" y="10" width="245" height="405" fill="url(#workerTones)" opacity="0.9" role="img" aria-label="Photo of a smiling roofer in a hard hat and hi-vis jacket, arms crossed"/>

    <polygon class="accent-line-top" points="1038,99 1200,4 1200,12 1052,99" fill="var(--white)"/>
    <polygon class="accent-line-bottom" points="800,439 968,338 968,346 814,439" fill="var(--white)"/>

    <polygon class="marker-up" points="730,195 748,164 766,195" fill="var(--white)"/>
    <polygon class="marker-down" points="1120,322 1142,322 1131,341" fill="var(--white)"/>

    <polygon class="call-bar" points="0,361 625,361 535,416 0,416" fill="var(--white)"/>

    <g class="social-dots">
      <circle cx="1006" cy="393" r="21" fill="var(--brand-red)"/>
      <circle cx="1066" cy="393" r="21" fill="var(--brand-red)"/>
      <circle cx="1125" cy="393" r="21" fill="var(--brand-red)"/>
    </g>
  </svg>

  <div class="brand">
    <span class="brand-name">STONECREST</span>
    <span class="brand-sub">ROOFING</span>
  </div>

  <p class="eyebrow">WE’RE HIRING</p>
  <h1 class="headline">NEW SALES</h1>
  <p class="market">IN OUR ALABAMA MARKET</p>
  <p class="pitch">"LET'S TALK ABOUT YOUR ROOF!"<br>SCHEDULE A FREE ROOF INSPECTION TODAY!</p>
  <p class="call-line">CALL : +00 418 270 395</p>
</main>
</body>
</html>
```